Web design for software company

I'm a software developer that designs high end specialist web applications, mobile apps and user friendly applications for medium to large customers. I integrate different systems together within a company and provide web based applications or mobile apps to view and edit information in that web of linked systems.

I currently work alone, basically selling my time on specialist projects, but also build my own software solutions which I eventually want to put into the market.

My company name is Quarrymind (lowercase 'L' for logic) and I work from the Netherlands. I've attached my current logo which is basically just text in VOXbox font. Current colours are mustard yellow and grey, but i'm open to other options to better fit the web design.

I've got a sort of slogan: "Specialized software development" - better ideas are welcome. The slogan in the logo attachment is older.

I'm looking for a site design that reflects my work as being on the cutting edge of technology, but being clear and simple. My thinking with the name Quarrymind is that it refers to the underlying mechanism and logic of software.

The site will not be text heavy, so some kind of large graphic to do with software design is welcome. I expect about 4 or 5 main pages or sections of the site in which i'll eventually add things like a blog or contact info etc.

Industry/Entity Type

It Company

Number of Pages Required

1 page

Font styles to use
Sans Serif

Requirements
Nice to have
• A large graphic or photo relevant to my focus as a software developer. Something that shows connecting of software systems with perhaps a variety of devices/browsers that would display data from that cloud of systems.
• Something like these (allthough these are ugly - but the idea is what i mean):
• http://st4.pixelvaultimg.example/2000817/22458/i/450/pixelvaultimg_224581193-Cloud-computing-user-interface.jpg
• http://business.tallwick.example/images/modules/mobile-device-policy-design-banner.png
• https://www.pagecrafta.example/images/responsive-web-design.jpg
• http://www.brevanto.example/images/web_apps.png
• https://www.keymurra.example/assets/img/product/web-app@2x.png?v2
Should not have
• Photographs of smiling happy people looking at a screen that make it look like it's a huge business with many offices. I'm a one-man company which could perhaps grow a little bit, but i want to focus on my expertise instead of size.

```html
<!DOCTYPE html>
<html lang="en">
<head>
<meta charset="utf-8">
<title>Quarrymind – Specialized Software Development</title>
<link rel="stylesheet" href="https://fonts.googleapis.com/css2?family=Lato:wght@400;700;900&family=Exo+2:wght@600&display=swap">
<style>
:root{
  --yellow:#f9d10f;
  --ink:#111111;
  --text:#2a2a2a;
  --muted:#555555;
  --light:#f2f2f2;
  --rule:#222222;
  --footer:#1f1f1f;
  --footer-deep:#0d0d0d;
  --footer-text:#d8d8d8;
  --white:#ffffff;
}
*{box-sizing:border-box;margin:0;padding:0}
html,body{width:1200px;height:2639px;overflow:hidden}
body{position:relative;background:var(--white);font-family:"Lato",sans-serif;color:var(--text)}
.abs{position:absolute}
section,header,footer{position:absolute;left:0;width:1200px}

/* header */
.site-header{top:0;height:123px;background:var(--white)}
.brand{left:100px;top:22px;font-family:"Lato",sans-serif;font-weight:900;font-size:36px;line-height:38px;color:var(--ink);letter-spacing:1px}
.contact-bar{right:106px;top:22px;display:flex;gap:18px;font-size:14px;color:var(--text);align-items:center}
.contact-bar span{display:flex;align-items:center;gap:8px}
.nav{left:347px;top:72px;display:flex;align-items:center;font-size:17px;letter-spacing:.3px;color:var(--ink)}
.nav a{color:inherit;text-decoration:none;padding:7px 16px;margin-right:9px}
.nav a.active{background:var(--yellow);border-radius:4px;font-weight:700}

/* hero */
.hero{top:123px;height:449px;background:linear-gradient(100deg,#f4f7f9 0%,#e6eef4 40%,#cddde8 70%,#e9f0f5 100%)}
.hero-title{left:100px;top:128px;font-family:"Exo 2",sans-serif;font-weight:600;font-size:44px;line-height:53px;color:var(--ink)}
.hero-visual{left:475px;top:17px;width:725px;height:388px;background:linear-gradient(160deg,#3b4656 0%,#9db3c6 45%,#e7eef3 100%);border-radius:4px;opacity:.85}

/* buttons */
.btn{display:flex;align-items:center;justify-content:space-between;border-radius:22px;font-weight:900;text-transform:uppercase;padding:0 6px 0 18px}
.btn .go{width:26px;height:26px;border-radius:50%;display:flex;align-items:center;justify-content:center}
.btn-dark{background:var(--ink);color:var(--white)}
.btn-dark .go{background:var(--yellow)}
.btn-yellow{background:var(--yellow);color:var(--ink)}
.btn-yellow .go{background:var(--ink)}

/* section headings */
.section-title{width:1200px;left:0;text-align:center;font-weight:900;font-size:28px;color:var(--ink);letter-spacing:.5px}
.divider{height:12px}
.divider .line{position:absolute;top:5px;height:2px;background:var(--rule)}
.divider i{position:absolute;top:0;width:12px;height:12px;border-radius:50%}
.divider i.small{width:9px;height:9px;top:1.5px;background:var(--yellow)}
.divider i.big{background:var(--ink)}

/* about */
.about{top:572px;height:449px;background:var(--white)}
.about-title{left:100px;top:86px;font-weight:900;font-size:28px;color:var(--ink)}
.about-copy{left:100px;top:167px;width:639px;font-size:13px;line-height:24px;color:var(--text)}
.about-photo{left:783px;top:53px;width:290px;height:396px;background:linear-gradient(180deg,#c9cdd2 0%,#8b8f95 55%,#4d5157 100%);border-radius:140px 140px 0 0}

/* services */
.services{top:1021px;height:431px;background:var(--light)}
.service{width:300px;text-align:center}
.service-icon{width:98px;height:98px;border-radius:50%;margin:0 auto;display:flex;align-items:center;justify-content:center}
.service h3{margin-top:30px;font-size:21px;font-weight:900;color:var(--ink)}
.service p{margin-top:10px;font-size:14px;line-height:22px;color:var(--text)}
.dot-trail{display:flex;align-items:center;gap:12px}
.dot-trail i{display:block;border-radius:50%;background:#dcdcdc}

/* specialized */
.specialized{top:1452px;height:436px;background:var(--white)}
.spec-visual{left:99px;top:153px;width:503px;height:234px;border:1px solid #dcdcdc;background:linear-gradient(120deg,#f7f7f7 0%,#d9d9d9 55%,#6a1d24 56%,#b3202c 75%,#e6e6e6 76%)}
.spec-lead{left:642px;top:163px;width:460px;font-weight:700;font-size:14px;line-height:22px;color:var(--ink)}
.checks{left:642px;top:226px;width:470px;display:grid;grid-template-columns:245px 225px;row-gap:22px}
.check{display:flex;gap:10px;font-size:13px;line-height:20px;color:var(--text)}

/* blog */
.blog{top:1888px;height:408px;background:var(--light)}
.post{width:471px;height:215px;background:var(--white);border:1px solid #e0e0e0}
.post-image{position:absolute;left:10px;top:12px;width:204px;height:189px}
.post-body{position:absolute;left:236px;top:22px;width:220px}
.post-body h4{font-size:13px;font-weight:700;text-decoration:underline;color:var(--ink)}
.post-body time{display:block;margin-top:12px;font-size:12px;font-weight:700;color:var(--yellow)}
.post-body p{margin-top:10px;font-size:12px;line-height:20px;color:var(--text)}
.post-body p b{color:var(--yellow);font-weight:400}
.pager{width:32px;height:32px;border-radius:50%;background:var(--white);border:1px solid #cfcfcf;display:flex;align-items:center;justify-content:center}

/* footer */
.site-footer{top:2296px;height:291px;background:var(--footer);color:var(--footer-text)}
.footer-title{font-size:21px;color:var(--white);font-weight:400}
.footer-title span{color:var(--yellow)}
.footer-title::after{content:"";display:block;width:100px;height:1px;background:#444;margin-top:10px}
.quick-links{list-style:none;font-size:13px;line-height:28.5px}
.quick-links li::before{content:"";display:inline-block;width:5px;height:5px;border-radius:50%;background:var(--yellow);margin-right:10px;vertical-align:middle}
.contact-details{font-size:13px;line-height:22px}
.contact-details .line{display:flex;align-items:center;gap:10px;margin-top:6px}
.inquiry input{display:block;width:232px;height:34px;border:0;margin-bottom:7px;padding:0 10px;font:13px "Lato",sans-serif;color:var(--ink);background:var(--white)}
.inquiry .submit{width:119px;height:34px;background:var(--yellow);border:0;font:700 16px "Lato",sans-serif;color:var(--ink);margin-top:2px}
.footer-brand{left:954px;top:95px;font-weight:900;font-size:36px;line-height:40px;color:var(--white)}
.socials{left:950px;top:194px;display:flex;gap:7px}
.socials i{display:block;width:32px;height:32px;border-radius:50%;background:var(--yellow)}
.copyright{top:2587px;height:52px;background:var(--footer-deep);color:#cfcfcf;font-size:12px;text-align:center;line-height:52px}
</style>
</head>
<body>

<header class="site-header">
  <div class="abs brand">QUARRY<br>MIND</div>
  <div class="abs contact-bar">
    <span>
      <svg width="22" height="22" viewBox="0 0 22 22"><circle cx="11" cy="11" r="10" fill="none" stroke="#f9d10f" stroke-width="2"/><path d="M7.5 6.5l2 .2.8 2.3-1.2 1a6 6 0 0 0 2.9 2.9l1-1.2 2.3.8.2 2a1.2 1.2 0 0 1-1.2 1.1A8 8 0 0 1 6.4 7.7a1.2 1.2 0 0 1 1.1-1.2z" fill="#111"/></svg>
      020 555 0148
    </span>
    <span>
      <svg width="22" height="22" viewBox="0 0 22 22"><circle cx="11" cy="11" r="10" fill="none" stroke="#f9d10f" stroke-width="2"/><rect x="6" y="7.5" width="10" height="7" fill="#111"/><path d="M6 7.5l5 4 5-4" fill="none" stroke="#fff" stroke-width="1"/></svg>
      inquiry@quarrymind.example
    </span>
  </div>
  <nav class="abs nav">
    <a class="active" href="#">HOME</a>
    <a href="#">ABOUT ME</a>
    <a href="#">OUR SERVICES</a>
    <a href="#">SOFTWARE SOLUTIONS</a>
    <a href="#">CONTACT US</a>
  </nav>
</header>

<section class="hero">
  <div class="abs hero-visual" role="img" aria-label="Row of screens and devices showing web application interfaces"></div>
  <h1 class="abs hero-title">High End Web<br>And Mobile<br>Applications</h1>
  <a class="abs btn btn-dark" style="left:100px;top:319px;width:217px;height:40px;font-size:20px;text-decoration:none">
    Get Started
    <span class="go"><svg width="10" height="12" viewBox="0 0 10 12"><path d="M2 1l6 5-6 5" fill="none" stroke="#111" stroke-width="2.4"/></svg></span>
  </a>
</section>

<section class="about">
  <h2 class="abs about-title">ABOUT ME</h2>
  <div class="abs divider" style="left:100px;top:131px;width:640px">
    <span class="line" style="left:0;width:562px"></span>
    <i class="small" style="left:584px"></i>
    <i class="big" style="left:606px"></i>
    <i class="small" style="left:631px"></i>
  </div>
  <p class="abs about-copy">Lorem ipsum dolor sit amet, consectetuer adipiscing elit, sed diam nonummy nibh euismod tincidunt ut laoreet dolore magna aliquam erat volutpat. Ut wisi enim ad minim veniam, quis nostrud exerci tation ullamcorper suscipit lobortis nisl ut aliquip ex ea commodo consequat. Duis autem vel eum iriure dolor in hendrerit in vulputate velit esse molestie consequat, vel illum dolore eu feugiat nulla facilisis at vero eros et accumsan et iusto odio dignissim qui blandit praesent luptatum zzril delenit augue duis dolore te feugait nulla facilisi. it praesent luptatum zzril delenit augue duis dolore te feugait.&nbsp; Lorem ipsum dolor sit amet, erat volutpat. Ut wisi enim ad minim veniam, quis nostrud exerci tation u.</p>
  <a class="abs btn btn-yellow" style="left:100px;top:357px;width:152px;height:37px;font-size:15px;text-decoration:none">
    Read More
    <span class="go"><svg width="9" height="11" viewBox="0 0 10 12"><path d="M2 1l6 5-6 5" fill="none" stroke="#fff" stroke-width="2.4"/></svg></span>
  </a>
  <div class="abs about-photo" role="img" aria-label="Portrait of the developer in a suit holding a tablet"></div>
</section>

<section class="services">
  <h2 class="abs section-title" style="top:46px">MY SERVICES</h2>
  <div class="abs divider" style="left:463px;top:101px;width:274px">
    <span class="line" style="left:0;width:104px"></span>
    <i class="small" style="left:107px"></i>
    <i class="big" style="left:131px"></i>
    <i class="small" style="left:158px"></i>
    <span class="line" style="left:170px;width:104px"></span>
  </div>

  <div class="abs dot-trail" style="left:382px;top:196px">
    <i style="width:10px;height:10px"></i><i style="width:14px;height:14px"></i><i style="width:18px;height:18px"></i><i style="width:22px;height:22px"></i>
  </div>
  <div class="abs dot-trail" style="left:708px;top:196px">
    <i style="width:10px;height:10px"></i><i style="width:14px;height:14px"></i><i style="width:18px;height:18px"></i><i style="width:22px;height:22px"></i>
  </div>

  <div class="abs service" style="left:107px;top:158px">
    <div class="service-icon" style="background:var(--ink)">
      <svg width="52" height="46" viewBox="0 0 52 46"><rect x="3" y="4" width="42" height="28" rx="2" fill="none" stroke="#fff" stroke-width="3"/><path d="M17 32v6h14v-6M12 40h24" stroke="#fff" stroke-width="3" fill="none"/><path d="M22 24l4-9 16-14 4 4-16 14z" fill="#fff"/></svg>
    </div>
    <h3>Web Applications</h3>
    <p>Lorem ipsum dolor sit amet,<br>consectetuer adipiscing elit sed<br>diamsit almet dolor</p>
  </div>
  <div class="abs service" style="left:450px;top:158px">
    <div class="service-icon" style="background:var(--yellow)">
      <svg width="40" height="56" viewBox="0 0 40 56"><rect x="8" y="4" width="22" height="46" rx="3" fill="none" stroke="#111" stroke-width="3"/><circle cx="19" cy="44" r="2" fill="#111"/><circle cx="24" cy="22" r="9" fill="none" stroke="#111" stroke-width="4" stroke-dasharray="4 3"/><circle cx="24" cy="22" r="3.5" fill="#111"/></svg>
    </div>
    <h3>Mobile Apps</h3>
    <p>Lorem ipsum dolor sit amet,<br>consectetuer adipiscing elit sed<br>diamsit almet dolor</p>
  </div>
  <div class="abs service" style="left:790px;top:158px">
    <div class="service-icon" style="background:var(--ink)">
      <svg width="52" height="46" viewBox="0 0 52 46"><path d="M4 26h12l4 6h12l4-6h12v16H4z" fill="#fff"/><path d="M14 24c2-10 10-14 20-14V4l12 11-12 11v-7c-8 0-14 1-20 5z" fill="#fff"/></svg>
    </div>
    <h3>User Friendly Applications</h3>
    <p>Lorem ipsum dolor sit amet,<br>consectetuer adipiscing elit sed<br>diamsit almet dolor</p>
  </div>
</section>

<section class="specialized">
  <h2 class="abs section-title" style="top:38px">SPECIALIZED SOFTWARE DEVELOPMENT</h2>
  <div class="abs divider" style="left:463px;top:96px;width:274px">
    <span class="line" style="left:0;width:104px"></span>
    <i class="small" style="left:107px"></i>
    <i class="big" style="left:131px"></i>
    <i class="small" style="left:158px"></i>
    <span class="line" style="left:170px;width:104px"></span>
  </div>
  <div class="abs spec-visual" role="img" aria-label="Tablet and phone on a white desk beside a cup of coffee"></div>
  <p class="abs spec-lead">Lorem ipsum dolor sit amet, consectetuer adipiscing elit, sed diamerri lonummy nibh euismod tincidunt ut laoreet dolore magna aliq</p>
  <div class="abs checks">
    <div class="check"><svg width="22" height="22" viewBox="0 0 22 22"><circle cx="11" cy="12" r="9" fill="var(--yellow)"/><path d="M5 11l5 5 10-13" fill="none" stroke="#111" stroke-width="2.6"/></svg><span>Lorem ipsum dolor sit amet er<br>consectet piscing elit</span></div>
    <div class="check"><svg width="22" height="22" viewBox="0 0 22 22"><circle cx="11" cy="12" r="9" fill="var(--yellow)"/><path d="M5 11l5 5 10-13" fill="none" stroke="#111" stroke-width="2.6"/></svg><span>Lorem ipsum dolor sit amet er<br>consectet piscing elit</span></div>
    <div class="check"><svg width="22" height="22" viewBox="0 0 22 22"><circle cx="11" cy="12" r="9" fill="var(--yellow)"/><path d="M5 11l5 5 10-13" fill="none" stroke="#111" stroke-width="2.6"/></svg><span>Lorem ipsum dolor sit amet er<br>consectet piscing elit</span></div>
    <div class="check"><svg width="22" height="22" viewBox="0 0 22 22"><circle cx="11" cy="12" r="9" fill="var(--yellow)"/><path d="M5 11l5 5 10-13" fill="none" stroke="#111" stroke-width="2.6"/></svg><span>Lorem ipsum dolor sit amet er<br>consectet piscing elit</span></div>
  </div>
  <a class="abs btn btn-yellow" style="left:642px;top:345px;width:178px;height:38px;font-size:15px;text-decoration:none">
    Call Me Today
    <span class="go"><svg width="9" height="11" viewBox="0 0 10 12"><path d="M2 1l6 5-6 5" fill="none" stroke="#fff" stroke-width="2.4"/></svg></span>
  </a>
</section>

<section class="blog">
  <h2 class="abs section-title" style="top:38px">LATEST BLOG POSTS</h2>
  <div class="abs divider" style="left:463px;top:91px;width:274px">
    <span class="line" style="left:0;width:104px"></span>
    <i class="small" style="left:107px"></i>
    <i class="big" style="left:131px"></i>
    <i class="small" style="left:158px"></i>
    <span class="line" style="left:170px;width:104px"></span>
  </div>

  <div class="abs pager" style="left:47px;top:232px"><svg width="10" height="12" viewBox="0 0 10 12"><path d="M7 1L2 6l5 5" fill="none" stroke="#666" stroke-width="1.6"/></svg></div>
  <div class="abs pager" style="left:1119px;top:232px"><svg width="10" height="12" viewBox="0 0 10 12"><path d="M3 1l5 5-5 5" fill="none" stroke="#666" stroke-width="1.6"/></svg></div>

  <article class="abs post" style="left:99px;top:144px">
    <div class="post-image" role="img" aria-label="Hand touching a glowing network of app icons" style="background:linear-gradient(135deg,#0a1a33 0%,#1b4f86 55%,#5fb0e6 100%)"></div>
    <div class="post-body">
      <h4>Ut tellus dolor, dapibus dollar</h4>
      <time>15Mar, 2016</time>
      <p>Duis autem vel eum iriure dolor in hendi rerit in vulputate velit essemo molestiel consequat, vel illum dolore eokfeuglatn nulla facilisis vero eros et accumsan eti iusto more dois mkiodio dignissim nulla facilisi... <b>[...]</b></p>
    </div>
  </article>
  <article class="abs post" style="left:630px;top:144px">
    <div class="post-image" role="img" aria-label="Person in white reaching toward a floating digital interface" style="background:linear-gradient(135deg,#1f7fc0 0%,#6fc0ea 50%,#dff1fb 100%)"></div>
    <div class="post-body">
      <h4>Ut tellus dolor, dapibus dollar</h4>
      <time>15Mar, 2016</time>
      <p>Duis autem vel eum iriure dolor in hendi rerit in vulputate velit essemo molestiel consequat, vel illum dolore eokfeuglatn nulla facilisis vero eros et accumsan eti iusto more dois mkiodio dignissim nulla facilisi... <b>[...]</b></p>
    </div>
  </article>
</section>

<footer class="site-footer">
  <div class="abs" style="left:100px;top:40px">
    <h3 class="footer-title">Quick <span>Links</span></h3>
    <ul class="quick-links" style="margin-top:10px">
      <li>Home</li><li>About Me</li><li>Services</li><li>Software Solutions</li><li>Contact Us</li>
    </ul>
  </div>
  <div class="abs contact-details" style="left:338px;top:40px;width:230px">
    <h3 class="footer-title">Contact <span>Details</span></h3>
    <div style="margin-top:14px;font-size:15px;color:var(--white)">QUARRYMIND</div>
    <div>123, Lorem ipsum dolor smit<br>amet, consectetuer dipis</div>
    <div class="line"><svg width="14" height="14" viewBox="0 0 14 14"><path d="M2.5 1l3 .3 1 3-1.6 1.4a8 8 0 0 0 4 4l1.4-1.6 3 1 .3 3a1.4 1.4 0 0 1-1.5 1.3A12 12 0 0 1 1.2 2.5 1.4 1.4 0 0 1 2.5 1z" fill="var(--yellow)"/></svg>020 555 0148</div>
    <div class="line"><svg width="14" height="10" viewBox="0 0 14 10"><rect width="14" height="10" fill="var(--yellow)"/><path d="M0 0l7 5 7-5" fill="none" stroke="#1f1f1f" stroke-width="1.2"/></svg>inquiry@quarrymind.example</div>
  </div>
  <div class="abs inquiry" style="left:611px;top:40px">
    <h3 class="footer-title">Quick <span>Inquiry</span></h3>
    <div style="margin-top:14px">
      <input type="text" placeholder="Name">
      <input type="text" placeholder="Email">
      <input type="text" placeholder="Message">
      <button class="submit" type="button">Submit</button>
    </div>
  </div>
  <div class="abs footer-brand">QUARRY<br>MIND</div>
  <div class="abs socials" aria-label="Social links"><i></i><i></i><i></i><i></i></div>
</footer>

<div class="abs copyright" style="left:0;width:1200px">Copyright © 2016 Quarrymind.&nbsp; All Rights Reserved.</div>

</body>
</html>
```